Create modern and sleek business card for luxury real estate company

We're a "boutique" real estate office looking for a design that gets across a highly modern luxury brand. Blacks and whites are probably the best colors unless we try a silver foil for the logo. I've attached a version of our current logo here. I'd like to swap out the current font on there with Gotham Light Regular.

I'm looking to have one side of the card have the logo with the space for our agents info on the other side.

Target Market(s)

Young professionals in a "luxury" headspace

Industry/Entity Type

Real estate

Contact Information for Business Card

A place for agent name, cell number, website. The slogan "Quietly Redefining Fine Homes".

Font styles to use
Other font styles liked:
• Gotham Regular

Colors

Designer to choose only greyscale colors for use in the design.

Requirements
Must have
• Matte black as the background color. Clean lines and use of contrast. A specific design aspect that will use silver foil.
Nice to have
• Up in the air on integrating a QR code
Should not have
• Any houses or other real estate related design (ex: a clip art house)

```html
<!DOCTYPE html>
<html lang="en">
<head>
<meta charset="utf-8">
<title>Halden Realty Business Card</title>
<link rel="stylesheet" href="https://fonts.googleapis.com/css2?family=Montserrat:wght@300;400;600&display=swap">
<style>
  :root {
    --bg: #161616;
    --card-white: #ffffff;
    --card-black: #1f1f1f;
    --ink: #141414;
    --muted: #9a9a9a;
    --contact: #6f6f6f;
    --icon: #555555;
    --rule: #bdbdbd;
    --emboss: #2b2b2b;
    --emboss-edge: #3a3a3a;
    --tagline: #b8b8b8;
  }
  * { box-sizing: border-box; margin: 0; padding: 0; }
  html, body { width: 1200px; height: 900px; overflow: hidden; }
  body {
    background: var(--bg);
    font-family: "Montserrat", sans-serif;
    display: flex;
    flex-direction: column;
    align-items: center;
    justify-content: center;
    gap: 56px;
  }
  .card {
    position: relative;
    width: 640px;
    height: 366px;
    border-radius: 18px;
    overflow: hidden;
  }
  /* Agent side */
  .card-front { background: var(--card-white); color: var(--ink); }
  .agent { position: absolute; left: 48px; top: 58px; }
  .agent-name { font-weight: 600; font-size: 21px; letter-spacing: 0.5px; text-transform: uppercase; }
  .agent-title { font-weight: 300; font-size: 15px; color: var(--muted); margin-top: 2px; }
  .agent-rule { width: 200px; height: 1px; background: var(--rule); margin: 14px 0 12px; }
  .contact { list-style: none; }
  .contact li {
    display: flex; align-items: center; gap: 10px;
    font-weight: 300; font-size: 14px; color: var(--contact); line-height: 22px;
  }
  .contact svg { width: 11px; height: 11px; flex: none; }
  .icon-fill { fill: var(--icon); }
  .icon-line { fill: none; stroke: var(--icon); stroke-width: 2.4; stroke-linejoin: round; }
  .brand {
    position: absolute; right: 54px; top: 130px;
    display: flex; align-items: center; gap: 14px;
  }
  .brand-mark { width: 52px; height: 52px; border: 2px solid currentColor; border-radius: 50%; flex: none; }
  .brand-name {
    font-weight: 400; font-size: 28px; letter-spacing: 3px; line-height: 1.05;
    text-transform: uppercase;
  }
  .card-rule {
    position: absolute; left: 48px; right: 48px; top: 246px;
    height: 1px; background: var(--rule);
  }
  .address {
    position: absolute; right: 54px; top: 262px;
    font-weight: 300; font-size: 14px; color: var(--muted); line-height: 21px;
  }
  /* Logo side */
  .card-back { background: var(--card-black); }
  .card-back .brand {
    right: auto; top: 120px; left: 50%; transform: translateX(-50%);
    color: var(--emboss);
    text-shadow: 0 1px 0 var(--emboss-edge);
  }
  .card-back .brand-mark { border-color: var(--emboss); box-shadow: 0 1px 0 var(--emboss-edge); }
  .card-back .brand-name { font-size: 34px; }
  .tagline {
    position: absolute; left: 0; right: 0; top: 262px; text-align: center;
    font-weight: 300; font-size: 14px; letter-spacing: 1px; color: var(--tagline);
  }
</style>
</head>
<body>
  <section class="card card-back">
    <div class="brand">
      <span class="brand-mark"></span>
      <span class="brand-name">Halden<br>Realty</span>
    </div>
    <p class="tagline">Quietly Redefining Fine Homes</p>
  </section>

  <section class="card card-front">
    <div class="agent">
      <h1 class="agent-name">Daniel Hart</h1>
      <p class="agent-title">Founder &amp; CEO</p>
      <div class="agent-rule"></div>
      <ul class="contact">
        <li><svg viewBox="0 0 24 24"><path class="icon-fill" d="M6.6 10.8a15 15 0 0 0 6.6 6.6l2.2-2.2a1 1 0 0 1 1-.25 11.4 11.4 0 0 0 3.6.57 1 1 0 0 1 1 1V20a1 1 0 0 1-1 1A17 17 0 0 1 3 4a1 1 0 0 1 1-1h3.5a1 1 0 0 1 1 1c0 1.25.2 2.45.57 3.57a1 1 0 0 1-.25 1z"/></svg>(555) 214-0397</li>
        <li><svg viewBox="0 0 24 24"><rect class="icon-line" x="2" y="5" width="20" height="14"/><path class="icon-line" d="M2 5l10 8 10-8"/></svg>hello@haldenrealty.com</li>
        <li><svg viewBox="0 0 24 24"><circle class="icon-line" cx="12" cy="12" r="10"/><path class="icon-line" d="M2 12h20M12 2c3 3 3 17 0 20M12 2c-3 3-3 17 0 20"/></svg>www.haldenrealty.com</li>
      </ul>
    </div>
    <div class="brand">
      <span class="brand-mark"></span>
      <span class="brand-name">Halden<br>Realty</span>
    </div>
    <div class="card-rule"></div>
    <p class="address">48 Linden Street Suite 310<br>Sample City, Country</p>
  </section>
</body>
</html>
```